We need a design for the front page of our website

A redesign of our website front page.
www.brookmarsh-media.net. We are looking for a cleaner bolder fresher look with the confines of the website header as we are redesigning the whole site.

Industry/Entity Type

Tv

Number of Pages Required

1 page

Colors
ffc214

```html
<!DOCTYPE html>
<html lang="en">
<head>
<meta charset="utf-8">
<title>Brookmarsh Media – Home</title>
<link href="https://fonts.googleapis.com/css2?family=Open+Sans:ital,wght@0,300;0,400;0,600;0,700;1,400&display=swap" rel="stylesheet">
<style>
:root{
  --orange:#f8b133;
  --orange-dark:#e9a226;
  --black:#0d0d0d;
  --footer:#111111;
  --ink:#222222;
  --muted:#777777;
  --light:#ececec;
  --panel:#e9e9e9;
  --line:#dddddd;
  --white:#ffffff;
  --grey-btn:#6d6d6d;
}
*{box-sizing:border-box;margin:0;padding:0}
html,body{width:1200px;height:2550px;overflow:hidden}
body{position:relative;background:var(--white);font-family:'Open Sans',Arial,sans-serif;color:var(--ink)}
.abs{position:absolute}
a{color:inherit;text-decoration:none}

/* top bar */
.topbar{left:0;top:0;width:1200px;height:48px;background:var(--black);color:#ddd;font-size:13px}
.topbar .phone{position:absolute;left:51px;top:14px;display:flex;align-items:center;gap:10px;font-size:15px;color:#fff}
.topbar .links{position:absolute;right:166px;top:17px;font-size:11px;letter-spacing:.1px;color:#ccc;white-space:nowrap}
.topbar .links .hl{color:var(--orange)}
.topbar .links span.sep{margin:0 6px}
.topbar .checkout{position:absolute;left:1047px;top:0;width:106px;height:48px;background:var(--orange);color:#fff;font-size:12px;display:flex;align-items:center;justify-content:center;gap:6px}

/* header */
.brand{left:52px;top:60px;display:flex;align-items:center;gap:14px}
.brand .mark{width:78px;height:78px;background:var(--orange)}
.brand .name{font-size:40px;font-weight:400;color:var(--ink);letter-spacing:-.5px}
.search{left:683px;top:94px;display:flex}
.search .field{width:280px;height:34px;border:1px solid #ccc;font-size:10px;color:#999;padding:10px 12px}
.search .btn{width:64px;height:34px;background:#222;color:#fff;font-size:11px;display:flex;align-items:center;justify-content:center}
.currency{left:1052px;top:94px;width:97px;height:34px;border:1px solid #ccc;font-size:10px;color:#999;padding:10px 10px}

/* nav */
.nav{left:0;top:160px;width:1200px;height:52px;background:var(--black)}
.cat-head{left:49px;top:160px;width:288px;height:52px;background:var(--orange);color:#fff;font-size:21px;display:flex;align-items:center;padding-left:28px;gap:18px}
.menu{left:337px;top:160px;height:52px;display:flex}
.menu li{list-style:none;height:52px;border-left:1px solid #333;display:flex;align-items:center;justify-content:center;color:#fff;font-size:11.5px;font-weight:600}

/* category list */
.cats{left:49px;top:212px;width:288px;background:var(--light)}
.cats li{list-style:none;height:57px;border-bottom:1px solid #dcdcdc;padding-left:22px;display:flex;align-items:center;font-size:14px;color:#444}

/* hero */
.hero{left:357px;top:235px;width:796px;height:467px;background:var(--light);overflow:hidden}
.hero .kicker{position:absolute;right:290px;top:118px;font-size:18px;font-style:italic;color:var(--orange)}
.hero .kicker b{font-weight:400;color:var(--ink)}
.hero .deal{position:absolute;right:290px;top:144px;font-size:44px;font-weight:700;color:var(--orange)}
.hero .sub{position:absolute;right:290px;top:215px;font-size:17px;color:var(--ink)}
.hero .rule{position:absolute;left:29px;top:248px;width:477px;height:1px;background:#999}
.hero .title{position:absolute;right:290px;top:258px;font-size:43px;font-weight:700;color:var(--ink);white-space:nowrap}
.hero .title span{color:var(--orange)}
.btn-orange{background:var(--orange);color:#fff;display:flex;align-items:center;justify-content:center;font-size:12px}
.btn-white{background:#fff;color:var(--orange);display:flex;align-items:center;justify-content:center;font-size:12px}
.hero .shop{position:absolute;left:199px;top:350px;width:144px;height:39px}
.hero .screen{position:absolute;left:520px;top:105px;width:260px;height:258px;background:linear-gradient(160deg,#7ab33a,#c8e08a 55%,#3e5f1c)}
.hero .dots{position:absolute;left:335px;top:437px;display:flex;gap:7px}
.hero .dots i{width:11px;height:5px;background:#aaa}
.hero .dots i.on{background:#222}

.divider{left:0;top:726px;width:1200px;height:1px;background:var(--line)}

/* sidebar blocks */
.block-head{width:237px;height:54px;background:var(--orange);color:#fff;font-size:15px;display:flex;align-items:center;justify-content:space-between;padding:0 22px}
.deal-item{width:237px;height:109px;background:var(--panel)}
.deal-item .tag{position:absolute;left:14px;top:-12px;width:36px;height:20px;background:var(--orange);color:#fff;font-size:10px;display:flex;align-items:center;justify-content:center}
.deal-item .thumb{position:absolute;left:12px;top:22px;width:88px;height:70px}
.deal-item .price{position:absolute;left:115px;top:24px;font-size:14px;color:var(--orange)}
.deal-item .price s{color:#444;text-decoration:none;margin-left:6px}
.deal-item .pname{position:absolute;left:115px;top:47px;font-size:12px;color:#555}
.deal-item .stars{position:absolute;left:115px;top:68px;font-size:9px;color:var(--orange);letter-spacing:1px}
.t-blue{background:linear-gradient(160deg,#1e6fd8,#86c8f5)}
.t-green{background:linear-gradient(160deg,#8fc4e8,#7dba3b)}
.t-dark{background:linear-gradient(160deg,#233a12,#8bbf3a)}
.t-flower{background:linear-gradient(160deg,#b32b4b,#3f7a2a)}
.t-beach{background:linear-gradient(160deg,#3c88c8,#c7e2f1 60%,#4c7a3a)}
.t-room{background:linear-gradient(160deg,#1d1d1d,#5a4a3a)}
.t-wall{background:linear-gradient(160deg,#2a2a2a,#8a7560 60%,#c9d6de)}

/* promos */
.promo{top:765px;width:400px;height:233px}
.promo .label{position:absolute;left:25px;top:40px;font-size:14px;color:#fff}
.promo .copy{position:absolute;left:25px;width:160px;font-size:12px;line-height:16px}
.promo .btn{position:absolute;left:17px;top:153px;width:99px;height:34px}
.promo .pic{position:absolute;top:55px;width:174px;height:113px}

/* products */
.section-title{left:335px;top:1042px;font-size:21px;color:var(--ink)}
.section-title span{color:var(--orange)}
.section-rule{left:335px;top:1080px;width:818px;height:2px;background:var(--line)}
.sortby{left:1061px;top:1040px;width:92px;height:32px;border:1px solid #ccc;font-size:10px;color:#444;display:flex;align-items:center;justify-content:center;gap:8px}
.card{width:253px;height:357px;border:1px solid #dedede;background:#fff}
.card .pic{position:absolute;left:55px;top:22px;width:144px;height:150px}
.card .pname{position:absolute;left:18px;top:222px;font-size:14px;color:#333}
.card .desc{position:absolute;left:18px;top:246px;width:220px;font-size:11px;line-height:15px;color:#888}
.card .price{position:absolute;left:18px;top:285px;font-size:19px;color:var(--orange);font-weight:600}
.card .price s{font-size:13px;color:#888;font-weight:400;margin-right:10px}
.card .actions{position:absolute;left:-1px;bottom:-1px;width:253px;height:36px;display:flex;font-size:11px;color:#fff}
.card .buy{width:120px;background:var(--orange);display:flex;align-items:center;padding-left:16px;gap:10px}
.card .cart{flex:1;background:var(--grey-btn);display:flex;align-items:center;padding-left:16px;gap:10px}
.chk{width:12px;height:12px;background:#fff;display:inline-block}

/* newsletter */
.newsletter{left:0;top:1887px;width:1200px;height:175px;background:#ebebeb}
.newsletter h2{position:absolute;right:722px;top:38px;font-size:37px;font-weight:300;color:var(--orange)}
.newsletter p{position:absolute;left:70px;top:90px;width:408px;font-size:13px;line-height:18px;color:#333;text-align:center}
.newsletter .email{position:absolute;left:518px;top:41px;width:247px;height:41px;background:#fff;border:1px solid #ccc;font-size:12px;color:#999;padding:12px 20px}
.newsletter .subscribe{position:absolute;left:518px;top:95px;width:247px;height:39px;background:#222;color:#fff;font-size:13px;display:flex;align-items:center;justify-content:center}
.newsletter .vrule{position:absolute;left:823px;top:22px;width:1px;height:130px;background:#ccc}
.social{position:absolute;width:44px;height:44px;border-radius:50%;border:2px solid var(--orange)}
.social.dark{border-color:#111}

/* features */
.features{left:0;top:2062px;width:1200px;height:133px;background:var(--orange)}
.feature{position:absolute;top:45px;display:flex;align-items:center;gap:22px;color:#fff;font-size:17px;font-weight:700;line-height:20px}
.features .sep{position:absolute;top:0;width:1px;height:133px;background:#e3a02c}

/* footer */
.footer{left:0;top:2195px;width:1200px;height:280px;background:var(--footer);color:#bbb}
.fcol{position:absolute;top:70px}
.fcol h4{font-size:13px;font-weight:700;color:#fff;margin-bottom:26px}
.fcol li{list-style:none;font-size:11px;color:#999;height:23px}
.contact-line{display:flex;gap:14px;font-size:11px;color:#bbb;line-height:22px;margin-bottom:16px}
.bottom{left:0;top:2475px;width:1200px;height:75px;background:var(--black)}
.bottom .copy{position:absolute;left:53px;top:31px;font-size:11px;color:#bbb}
.cardmark{position:absolute;top:22px;width:44px;height:30px;background:#fff;border-radius:3px}
</style>
</head>
<body>

<div class="abs topbar">
  <div class="phone">
    <svg width="14" height="16" viewBox="0 0 14 16"><path d="M3 1 L6 4 L4.5 6 C5.5 8.5 7 10 9.5 11.5 L11.5 10 L14 13 L12 15.5 C6 15 1 9 .5 3.5 Z" fill="#f8b133"/></svg>
    1800 5550 123
  </div>
  <div class="links"><a class="hl">LOGIN/REGISTER</a><span class="sep">|</span>MY ACCOUNT<span class="sep">|</span>WISHLIST - 0<span class="sep">|</span>SHOPPING TV - <span class="hl">$0.0</span></div>
  <a class="checkout">CHECKOUT
    <svg width="14" height="10" viewBox="0 0 14 10"><path d="M0 3h8V0l6 5-6 5V7H0z" fill="#fff"/></svg>
  </a>
</div>

<div class="abs brand"><div class="mark"></div><div class="name">Brookmarsh</div></div>
<div class="abs search"><div class="field">Enter keyword</div><div class="btn">SEARCH</div></div>
<div class="abs currency">US Dollar $ &nbsp;&nbsp;⌄</div>

<div class="abs nav"></div>
<div class="abs cat-head">
  <svg width="26" height="16" viewBox="0 0 26 16"><rect width="26" height="3" fill="#fff"/><rect y="6.5" width="26" height="3" fill="#fff"/><rect y="13" width="26" height="3" fill="#fff"/></svg>
  CATEGORIES
</div>
<ul class="abs menu">
  <li style="width:68px"><svg width="20" height="18" viewBox="0 0 20 18"><path d="M10 0 L20 9 H17 V18 H12 V12 H8 V18 H3 V9 H0 Z" fill="#fff"/></svg></li>
  <li style="width:100px">ABOUT US</li>
  <li style="width:105px">SHIPPING</li>
  <li style="width:105px">RETURNS</li>
  <li style="width:90px">FAQ</li>
  <li style="width:88px">BLOG</li>
  <li style="width:90px">EVENTS</li>
  <li style="width:170px;border-right:1px solid #333">CONTACT US</li>
</ul>

<ul class="abs cats">
  <li>LED TV</li><li>LCD TV</li><li>LARGE TYPE</li><li>SHORT TYPE</li>
  <li>LED TV</li><li>LCD TV</li><li>LARGE TYPE</li><li>SHORT TYPE</li>
  <li style="border-bottom:none">NEW MODEL TV</li>
</ul>

<section class="abs hero">
  <div class="kicker">Latest model Tv <b>Offers</b></div>
  <div class="deal">25% OFF</div>
  <div class="sub">THE MARKED PRICE OF</div>
  <div class="rule"></div>
  <div class="title">SUMMER <span>HOT OFFERS</span></div>
  <a class="shop btn-orange">SHOP NOW</a>
  <div class="screen" role="img" aria-label="Flat screen television showing daisies in a meadow"></div>
  <div class="dots"><i class="on"></i><i></i><i></i><i></i></div>
</section>

<div class="abs divider"></div>

<div class="abs block-head" style="left:49px;top:755px">SPECIALS <span style="font-size:11px">⌄ ⌃</span></div>
<div class="abs deal-item" style="left:49px;top:836px"><span class="tag">SALE</span><div class="thumb t-blue" role="img" aria-label="Television with blue screen"></div><div class="price">$150.00<s>$199.99</s></div><div class="pname">MAURIS GRAVIDA</div><div class="stars">★★★★★</div></div>
<div class="abs deal-item" style="left:49px;top:971px"><span class="tag">SALE</span><div class="thumb t-green" role="img" aria-label="Television showing a green field"></div><div class="price">$150.00<s>$199.99</s></div><div class="pname">MAURIS GRAVIDA</div><div class="stars">★★★★★</div></div>
<div class="abs deal-item" style="left:49px;top:1108px"><span class="tag">SALE</span><div class="thumb t-dark" role="img" aria-label="Television showing grass"></div><div class="price">$150.00<s>$199.99</s></div><div class="pname">MAURIS GRAVIDA</div><div class="stars">★★★★★</div></div>
<div class="abs deal-item" style="left:49px;top:1243px"><span class="tag">SALE</span><div class="thumb t-flower" role="img" aria-label="Television showing a flower"></div><div class="price">$150.00<s>$199.99</s></div><div class="pname">MAURIS GRAVIDA</div><div class="stars">★★★★★</div></div>

<div class="abs block-head" style="left:49px;top:1380px">BESTSELLERS <span style="font-size:11px">⌄ ⌃</span></div>
<div class="abs deal-item" style="left:49px;top:1457px"><span class="tag">SALE</span><div class="thumb t-blue" role="img" aria-label="Television with blue screen"></div><div class="price">$150.00<s>$199.99</s></div><div class="pname">MAURIS GRAVIDA</div><div class="stars">★★★★★</div></div>
<div class="abs deal-item" style="left:49px;top:1593px"><span class="tag">SALE</span><div class="thumb t-green" role="img" aria-label="Television showing a green field"></div><div class="price">$150.00<s>$199.99</s></div><div class="pname">MAURIS GRAVIDA</div><div class="stars">★★★★★</div></div>
<div class="abs deal-item" style="left:49px;top:1729px"><span class="tag">SALE</span><div class="thumb t-dark" role="img" aria-label="Television showing grass"></div><div class="price">$150.00<s>$199.99</s></div><div class="pname">MAURIS GRAVIDA</div><div class="stars">★★★★★</div></div>

<div class="abs promo" style="left:335px;background:var(--orange)">
  <div class="label">TV &amp; VIDEO</div>
  <div class="copy" style="top:68px;color:#fff">Lorem ipsum dolor sit amet, consectetur adipi-scing elit, sed do eius-mod tempor</div>
  <a class="btn btn-white" style="top:153px">SHOP NOW</a>
  <div class="pic t-beach" style="left:195px" role="img" aria-label="Television showing a tropical beach"></div>
</div>
<div class="abs promo" style="left:753px;background:var(--panel)">
  <div class="copy" style="top:68px;color:#333">Lorem ipsum dolor sit amet, consectetur adipi-scing elit, sed do eius-mod tempor</div>
  <a class="btn btn-orange" style="top:153px">SHOP NOW</a>
  <div class="pic t-flower" style="left:185px" role="img" aria-label="Television showing a butterfly on a flower"></div>
</div>

<div class="abs section-title"><span>NEW</span> PRODUCTS</div>
<div class="abs sortby">SORT BY <span>⌄</span></div>
<div class="abs section-rule"></div>

<div class="abs card" style="left:333px;top:1105px"><div class="pic t-wall" role="img" aria-label="Wall mounted television"></div><div class="pname">Name of the product</div><div class="desc">Lorem ipsum dolor sit amet conse ctetur adipiscing elit, sed do eiusmodaliqua.</div><div class="price"><s>$35.00</s>$ 29.00</div><div class="actions"><span class="buy"><i class="chk"></i>BUY NOW</span><span class="cart"><i class="chk"></i>ADD TO CART</span></div></div>
<div class="abs card" style="left:614px;top:1105px"><div class="pic t-room" role="img" aria-label="Black television on a stand"></div><div class="pname">Name of the product</div><div class="desc">Lorem ipsum dolor sit amet conse ctetur adipiscing elit, sed do eiusmodaliqua.</div><div class="price"><s>$35.00</s>$ 29.00</div><div class="actions"><span class="buy"><i class="chk"></i>BUY NOW</span><span class="cart"><i class="chk"></i>ADD TO CART</span></div></div>
<div class="abs card" style="left:898px;top:1105px"><div class="pic t-green" role="img" aria-label="Television showing a tree in a field"></div><div class="pname">Name of the product</div><div class="desc">Lorem ipsum dolor sit amet conse ctetur adipiscing elit, sed do eiusmodaliqua.</div><div class="price"><s>$35.00</s>$ 29.00</div><div class="actions"><span class="buy"><i class="chk"></i>BUY NOW</span><span class="cart"><i class="chk"></i>ADD TO CART</span></div></div>

<div class="abs card" style="left:333px;top:1491px"><div class="pic t-wall" role="img" aria-label="Wall mounted television"></div><div class="pname">Name of the product</div><div class="desc">Lorem ipsum dolor sit amet conse ctetur adipiscing elit, sed do eiusmodaliqua.</div><div class="price"><s>$35.00</s>$ 29.00</div><div class="actions"><span class="buy"><i class="chk"></i>BUY NOW</span><span class="cart"><i class="chk"></i>ADD TO CART</span></div></div>
<div class="abs card" style="left:614px;top:1491px"><div class="pic t-room" role="img" aria-label="Black television on a stand"></div><div class="pname">Name of the product</div><div class="desc">Lorem ipsum dolor sit amet conse ctetur adipiscing elit, sed do eiusmodaliqua.</div><div class="price"><s>$35.00</s>$ 29.00</div><div class="actions"><span class="buy"><i class="chk"></i>BUY NOW</span><span class="cart"><i class="chk"></i>ADD TO CART</span></div></div>
<div class="abs card" style="left:898px;top:1491px"><div class="pic t-green" role="img" aria-label="Television showing a tree in a field"></div><div class="pname">Name of the product</div><div class="desc">Lorem ipsum dolor sit amet conse ctetur adipiscing elit, sed do eiusmodaliqua.</div><div class="price"><s>$35.00</s>$ 29.00</div><div class="actions"><span class="buy"><i class="chk"></i>BUY NOW</span><span class="cart"><i class="chk"></i>ADD TO CART</span></div></div>

<section class="abs newsletter">
  <h2>Newsletter Sign Up</h2>
  <p>Lorem ipsum dolor sit amet conse ctetur adipiscing elit, sed do eius-mod tempor incididunt ut labore et dolore magna aliqua.</p>
  <div class="email">ENTER YOUR EMAIL ADDRESS</div>
  <a class="subscribe">SUBSCRIBE</a>
  <div class="vrule"></div>
  <span class="social dark" style="left:891px;top:34px"></span>
  <span class="social" style="left:954px;top:34px"></span>
  <span class="social" style="left:1032px;top:34px"></span>
  <span class="social" style="left:891px;top:94px"></span>
  <span class="social" style="left:954px;top:94px"></span>
  <span class="social" style="left:1032px;top:94px"></span>
</section>

<section class="abs features">
  <div class="feature" style="left:82px">
    <svg width="42" height="42" viewBox="0 0 42 42"><path d="M2 18h8v22H2z M13 18 L21 3 c3 0 5 2 4 6 l-2 7 h13 c3 0 5 3 4 6 l-4 14 c-1 3-3 4-6 4 H13z" fill="#fff"/></svg>
    <div>SATISFACTION<br>100% GUARANTEED</div>
  </div>
  <div class="sep" style="left:386px"></div>
  <div class="feature" style="left:468px">
    <svg width="46" height="34" viewBox="0 0 46 34"><path d="M0 2h28v22H0z M30 9h9l7 9v6H30z" fill="#fff"/><circle cx="9" cy="28" r="5" fill="#fff"/><circle cx="37" cy="28" r="5" fill="#fff"/></svg>
    <div>FREE SHIPPING<br>ON ORDERS OVER $99</div>
  </div>
  <div class="sep" style="left:782px"></div>
  <div class="feature" style="left:842px">
    <svg width="40" height="40" viewBox="0 0 40 40"><path d="M20 5a15 15 0 0 1 14 10" stroke="#fff" stroke-width="6" fill="none"/><path d="M38 8 L36 20 L26 14z" fill="#fff"/><path d="M20 35a15 15 0 0 1-14-10" stroke="#fff" stroke-width="6" fill="none"/><path d="M2 32 L4 20 L14 26z" fill="#fff"/></svg>
    <div>7 DAY<br>EASY RETURN</div>
  </div>
</section>

<footer class="abs footer">
  <div class="fcol" style="left:53px"><h4>INFORMATION</h4><ul><li>ABOUT US</li><li>CUSTOMER SERVICE</li><li>PRIVACY POLICY</li><li>SEARCH TERMS</li><li>ORDERS AND RETURNS</li><li>CONTACT US</li></ul></div>
  <div class="fcol" style="left:323px"><h4>WHY BUY FROM US</h4><ul><li>SHIPPING &amp; RETURNS</li><li>SECURE SHOPPING</li><li>INTERNATIONAL SHIPPING</li><li>AFFILIATES</li><li>GROUP SALES</li></ul></div>
  <div class="fcol" style="left:626px"><h4>MY ACCOUNT</h4><ul><li>SIGN IN</li><li>VIEW CART</li><li>MY WISHLIST</li><li>TRACK MY ORDER</li><li>HELP</li></ul></div>
  <div class="fcol" style="left:869px"><h4>CONTACTS</h4>
    <div class="contact-line"><svg width="10" height="14" viewBox="0 0 10 14"><path d="M5 0a5 5 0 0 1 5 5c0 4-5 9-5 9S0 9 0 5a5 5 0 0 1 5-5z" fill="#999"/><circle cx="5" cy="5" r="2" fill="#111"/></svg><div>212 KESTREL LANE, HARWICK HK2 7LD<br>P. O BOX 40871, COUNTRY</div></div>
    <div class="contact-line"><svg width="12" height="14" viewBox="0 0 14 16"><path d="M3 1 L6 4 L4.5 6 C5.5 8.5 7 10 9.5 11.5 L11.5 10 L14 13 L12 15.5 C6 15 1 9 .5 3.5 Z" fill="#999"/></svg><div>CALL US: (800) 5550-1942</div></div>
    <div class="contact-line" style="margin-top:-12px"><svg width="12" height="10" viewBox="0 0 12 10"><rect width="12" height="10" fill="#999"/><path d="M0 0 L6 5 L12 0" stroke="#111" fill="none"/></svg><div>EMAIL INFO@BROOKMARSH-MEDIA.NET</div></div>
  </div>
</footer>
<div class="abs bottom">
  <div class="copy">All Rights Reserved. Copyrights @ 2016</div>
  <span class="cardmark" style="left:998px"></span>
  <span class="cardmark" style="left:1048px"></span>
  <span class="cardmark" style="left:1098px"></span>
</div>

</body>
</html>
```